Exciting Poster Project: 4 posters for Employee Benefit Program

We are an entrepreneurial healthcare IT company that is creating an internal campaign to launch our 2017 Culture and Professional Development goals for our internal staff.

We need 4 posters utilizing the 4 campaign logos (attached) that are tied together visually into a cohesive campaign.

A PPT is included that shows the other wall art that currently exists on the walls. The new posters will share a space with these pieces.

The posters may be mounted side by side, or stand alone on a wall- so the design should work both ways. Each poster should include its own icon and the tag line provided along with topics provided that fall under this category. The posters size can be dictated by your design, but the text should be legible from a minimum of 8 feet away.

At the bottom of each poster should include all 4 icons in order to tie the entire campaign together (perhaps they can be arranged together like a diamond shape with the primary one as the biggest diamond)

Our company website for our external branding is: www.pelmaroq.com
We have included our branding guidelines for our external brand, and ppts and graphics for our internal brand.

1) Poster 1:
a. Header: Better Today Than Yesterday
b. Sub-title: Personal and Professional Growth
c. Description: We are committed to helping you build on your strengths and passions and support you your career advancement goals. We have a variety of training and development programs available to help you reach your top potential!
Leadership Development Programs
1. Supervisor Training
2. Women’s Leadership
3. Leadership Meet-Ups
4. MBA Program
Staff Development
1. Continuing Education Fund
2. Book Club
3. Pelmaroq University
4. Mentorship
5. Learning Libraries
6. Department Wide Training Events

2) Poster 2:
a. Header: Perform at Highest Capacity
b. Sub-title: Be Your Best Self
c. Description: We are committed to providing programs that bring focus to your health and overall personal wellness to encourage a well balanced life
i. Healthy Living
1. Health and wellness seminars
2. Nutrition: Fruit Delivery
ii. Fitness:
1. Step Challenge
2. Virtual 5k
3. Recess
4. Golf Lessons
5. Ping Pong Club
iii. Creativity:
1. Painting
2. Photography Club
3. Virtual Trivia
iv. Mental Health:
1. Massage Therapy
2. EAP Education
v. Financial
1. 401(k)
2. Retirement education/financial planning seminars
3. Global Insurance Program education

3) Poster 3:
a. Header: Passionate Urgent and Driven to Success
b. Sub-Header: Innovation and Strategy
c. Description: We are committed to helping you connect the dots both in the industry and with our internal goals , mission, and vision.
i. Quarterly All-Hands
ii. Lumiverse
1. Internally: Departmental and Product Updates
2. Externally: Industry Knowledge
3. Culturally: Peer to Peer Community

4) Poster 4:
a. Header: Succeed as a Team
b. Sub-Header: Cultivating Collaboration
c. Description: We are committed to creating a culture of appreciation, teamwork, and supporting an open communication. All feedback and ideas are welcome here!
i. Team Building Events
1. Employee Focused
a. Summer Picnic
b. Employee Appreciation
c. Diwali
d. Holiday Party
e. Department Appreciation
2. Family Friendly
a. Halloween
b. Bring your Kids to Work Day
3. Awards
a. Peer to Peer: QuickNod Awards
b. Leadership: Crest of Merit
4. Surveys
a. New Hire
b. Employee Engagement
Updates

Target Market(s)

Internal Employees

Industry/Entity Type

Healthcare

Font styles to use
Sans Serif

Requirements
Must have
• Job Type: Posters
• Task Outline: Create Vector Art for 4 icons and 4 posters
• Fonts and Styles to Use: SourceSansPro
Nice to have
• There is an attachment with suggested concepts and styles that we like.
Should not have
• The poster should not be very wordy or hard to read in passing.

```html
<!DOCTYPE html>
<html lang="en">
<head>
<meta charset="utf-8">
<title>Better Today Than Yesterday – Poster</title>
<link rel="stylesheet" href="https://fonts.googleapis.com/css2?family=Bebas+Neue&family=Patrick+Hand+SC&display=swap">
<style>
  :root {
    --canvas: #e6e7e8;
    --green-light: #a6d064;
    --green-mid: #7fb443;
    --green-dark: #2f5a1c;
    --green-darker: #22441a;
    --paper: #f4f8ec;
    --white: #ffffff;
    --ink: #2a4a17;
    --text-soft: #c9e8a0;
    --brand-orange: #e2572b;
  }
  * { box-sizing: border-box; margin: 0; padding: 0; }
  html, body { width: 1200px; height: 623px; overflow: hidden; }
  body { background: var(--canvas); position: relative; font-family: "Patrick Hand SC", cursive; }

  .poster {
    position: absolute; left: 410px; top: 19px;
    width: 380px; height: 585px; overflow: hidden;
    background: var(--green-mid);
    box-shadow: 0 6px 18px rgba(0,0,0,.18);
  }
  .poster__bands { position: absolute; inset: 0; width: 100%; height: 100%; }

  .brand { position: absolute; left: 18px; top: 14px; display: flex; align-items: center; gap: 6px; }
  .brand__mark { width: 22px; height: 22px; background: var(--brand-orange); }
  .brand__name { font-family: "Bebas Neue", sans-serif; font-size: 17px; color: var(--ink); letter-spacing: .5px; }

  .headline { position: absolute; font-family: "Bebas Neue", sans-serif; color: var(--white);
    text-shadow: 3px 3px 0 rgba(30,60,15,.45); line-height: .9; white-space: nowrap; font-weight: 400; }
  .headline--better { left: 124px; top: 46px; font-size: 66px; }
  .headline--today { left: 124px; top: 103px; font-size: 58px; }
  .headline--today small { font-size: 26px; }
  .headline--yesterday { left: 162px; top: 156px; font-size: 56px; }

  .mascot { position: absolute; left: 58px; top: 112px; width: 48px; height: 38px;
    background: var(--green-light); border-radius: 50%; }
  .subtitle { position: absolute; left: 16px; top: 156px; width: 140px; text-align: center;
    color: var(--ink); font-size: 18px; line-height: 1.1; }
  .subtitle__and { display: block; font-size: 12px; }
  .subtitle__growth { display: inline-block; margin-top: 8px; padding: 2px 14px;
    border: 2px solid var(--ink); border-radius: 10px; font-size: 28px; }

  .section-title { position: absolute; font-size: 15px; white-space: nowrap; font-weight: 400;
    transform-origin: left center; }
  .section-title--leadership { left: 18px; top: 316px; color: var(--green-dark); transform: rotate(-8deg); }
  .section-title--staff { left: 186px; top: 402px; color: var(--white); font-size: 16px; transform: rotate(-6deg); }

  .program-list { position: absolute; list-style: none; transform: rotate(-8deg); transform-origin: left top; white-space: nowrap; }
  .program-list--leadership { left: 26px; top: 356px; color: var(--white); font-size: 18px; line-height: 24px; }
  .program-list--staff { left: 28px; top: 470px; color: var(--text-soft); font-size: 12px; line-height: 16px; }
</style>
</head>
<body>
  <article class="poster">
    <svg class="poster__bands" viewBox="0 0 380 585" aria-hidden="true">
      <defs>
        <linearGradient id="field" x1="0" y1="0" x2="1" y2="1">
          <stop offset="0" stop-color="#b5da78"/>
          <stop offset="1" stop-color="#6ea83a"/>
        </linearGradient>
      </defs>
      <rect width="380" height="585" fill="url(#field)"/>
      <polygon points="0,0 215,0 0,170" fill="#eef6df"/>
      <polygon points="215,0 380,0 380,250 260,170" fill="#5e9632" opacity=".85"/>
      <polygon points="120,0 215,0 120,80" fill="#d7ebb6"/>
      <polygon points="0,303 380,258 380,292 0,347" fill="#f4f8ec"/>
      <line x1="0" y1="352" x2="380" y2="298" stroke="#f4f8ec" stroke-width="2" stroke-dasharray="5 4"/>
      <line x1="180" y1="430" x2="380" y2="406" stroke="#f4f8ec" stroke-width="2" stroke-dasharray="5 4"/>
      <polygon points="0,455 380,418 380,575 0,575" fill="var(--green-dark)"/>
      <polygon points="0,575 380,575 380,585 0,585" fill="#8cc04f"/>
      <g fill="#ffffff">
        <polygon points="224,275 242,275 264,327 242,380 224,380 246,327"/>
        <polygon points="249,275 267,275 289,327 267,380 249,380 271,327"/>
        <polygon points="274,275 292,275 314,327 292,380 274,380 296,327"/>
      </g>
      <g fill="var(--green-darker)">
        <polygon points="280,430 298,430 322,482 298,535 280,535 304,482"/>
        <polygon points="305,430 323,430 347,482 323,535 305,535 329,482"/>
        <polygon points="330,430 348,430 372,482 348,535 330,535 354,482"/>
      </g>
    </svg>

    <div class="brand"><span class="brand__mark"></span><span class="brand__name">Pelmaroq</span></div>

    <h1>
      <span class="headline headline--better">Better</span>
      <span class="headline headline--today">Today <small>than</small></span>
      <span class="headline headline--yesterday">Yesterday</span>
    </h1>

    <div class="mascot" role="img" aria-label="Cartoon character illustration"></div>
    <p class="subtitle">Personal<span class="subtitle__and">and</span>Professional<br><span class="subtitle__growth">Growth</span></p>

    <h2 class="section-title section-title--leadership">Leadership Development Programs</h2>
    <ol class="program-list program-list--leadership">
      <li>1. Supervisor Training</li>
      <li>2. Women's Leadership</li>
      <li>3. Leadership Meet-Ups</li>
      <li>4. MBA Program</li>
    </ol>

    <h2 class="section-title section-title--staff">Staff Development</h2>
    <ol class="program-list program-list--staff">
      <li>1. Continuing Education Fund</li>
      <li>2. Book Club</li>
      <li>3. Pelmaroq University</li>
      <li>4. Mentorship</li>
      <li>5. Learning Libraries</li>
      <li>6. Department Wide Training Events</li>
    </ol>
  </article>
</body>
</html>
```